New to ArtHarbor? This contest is for you!

Are you new to ArtHarbor and looking to enter your first contest? Look no further!

We're launching this special contest to help you get started on building a design portfolio at ArtHarbor!

Requirements:
Create a mini one-page portfolio featuring selection of 3-5 designs from your personal portfolio to sell yourself as a designer.

The submission (1 page portfolio) should showcase your design skills to our design quality team and to our designers.

We've mocked up a few layouts to provide a guide for how to layout your submission. Please see the attachments to the brief. (This is a guide only.)

The mini portfolio should grab attention and communicate who your personal design brand.

Designers are limited to 1 design submission, so show us your best work!

You must upload your entry before 12:00am 1 Oct 2016 UTC

This must be your very FIRST entry on ArtHarbor to be eligible to receive a prize. If you've already entered other ArtHarbor contests you won't be eligible to win the prizes.

Your design must adhere to our quality standards and be approved by our quality team to be eligible to receive a prize.

Target Market(s)

ArtHarbor quality team
ArtHarbor customers

Industry/Entity Type

Graphic Design

Requirements
Must have
• Showcase 3-5 of your best designs from your personal work on 1 page.
• The portfolio should grab our judges attention and communicate who you are as a designer.
Nice to have
• Text or descriptions about the work is optional
Should not have
• No individual design examples should be submitted.

```html
<!DOCTYPE html>
<html lang="en">
<head>
<meta charset="utf-8">
<title>Mini Portfolio – Web Design</title>
<link href="https://fonts.googleapis.com/css2?family=Oswald:wght@400;500;700&family=Open+Sans:wght@400;600;700&display=swap" rel="stylesheet">
<style>
:root{
  --page:#ffffff;
  --pattern:#eceef1;
  --cyan:#3cc6dc;
  --cyan-dark:#21a9c0;
  --dark:#2a2b2e;
  --lime:#dfe83a;
  --peach:#f6c6b3;
  --teal:#5fd3d6;
  --mint:#7ee0cc;
  --orange:#ef5a2c;
  --gold:#b08a2c;
  --yellow:#f2b232;
  --grey:#8c8f94;
  --text:#55585d;
}
*{margin:0;padding:0;box-sizing:border-box}
html,body{width:800px;height:1200px;overflow:hidden;background:var(--page)}
body{position:relative;font-family:"Open Sans",sans-serif;color:var(--dark)}
.abs{position:absolute}
.backdrop{position:absolute;background:radial-gradient(circle at 30% 30%,#f5f6f8,var(--pattern))}
.site{position:absolute;overflow:hidden;background:#fff}
.photo{position:absolute;left:0;width:100%}
.tiny{font-size:2.6px;line-height:1.5;color:var(--text)}
.center{text-align:center}
.caps{text-transform:uppercase;font-weight:700}
.btn{position:absolute;height:4px;font-size:1.9px;line-height:4px;text-align:center;color:#fff;font-weight:700;text-transform:uppercase}

/* fitness */
.feature{position:absolute;width:44px;text-align:center}
.feature .dot{display:block;margin:0 auto 2px;width:9px;height:9px;border-radius:50%;background:var(--cyan)}
.feature b{display:block;font-size:2.4px;color:var(--cyan);text-transform:uppercase}
.feature span{display:block;font-size:2.1px;color:#8a8d92;line-height:1.5;margin-top:1px}
.bullets{position:absolute;font-size:2.2px;color:#dfe2e6;line-height:1.8}
.activity{position:absolute;width:28px;text-align:center}
.activity .dot{display:block;margin:0 auto 2px;width:9px;height:9px;border-radius:50%;background:var(--cyan)}
.activity b{font-size:2.1px;color:var(--cyan);text-transform:uppercase}

/* tires */
.t-head{font-family:"Oswald",sans-serif;font-weight:500;text-transform:uppercase}
.t-cell{position:absolute;width:48px;height:52px;font-family:"Oswald",sans-serif;font-size:2.7px;color:#fff;text-align:center;padding:17px 4px 0;text-transform:uppercase;line-height:1.3}
.t-cell i{display:block;margin:0 auto 3px;width:5px;height:5px;border-radius:50%;background:#fff}
.faq{position:absolute;left:76px;width:176px;height:8px;border:0.8px solid #e3e3e3;font-size:2.4px;line-height:6.4px;padding:0 4px;color:#444;font-weight:600}
.faq::after{content:"";position:absolute;right:-0.8px;top:-0.8px;width:8px;height:8px;background:var(--yellow)}
.nav{position:absolute;font-family:"Oswald",sans-serif;font-size:2.6px;color:#fff;text-transform:uppercase}
</style>
</head>
<body>

<div class="backdrop" style="left:54px;top:62px;width:328px;height:487px" role="img" aria-label="Light grey network pattern with person icons"></div>
<div class="backdrop" style="left:54px;top:590px;width:328px;height:486px" role="img" aria-label="Light grey network pattern with person icons"></div>
<div class="backdrop" style="left:420px;top:62px;width:328px;height:1014px" role="img" aria-label="Light grey network pattern with person icons"></div>

<!-- Fitness website -->
<section class="site fitness" style="left:142px;top:62px;width:152px;height:485px">
  <div class="photo" style="top:0;height:82px;background:linear-gradient(115deg,#5e574c,#b59a76 35%,#d9c19b 55%,#8f7e67 80%,#c7a35a)" role="img" aria-label="Trainer coaching a woman on a gym machine"></div>
  <div class="abs" style="left:24px;top:4px;font-size:3.4px;color:#fff;font-weight:700;letter-spacing:.2px">PEAK FORM</div>
  <div class="abs" style="left:24px;top:8px;font-size:1.9px;color:#e6f8fb">HOME FITNESS</div>
  <div class="btn" style="right:6px;top:5px;width:13px;background:var(--cyan)">Join</div>
  <div class="abs center" style="top:52px;width:100%;font-size:4.4px;font-weight:700;color:#fff">IN-HOME PERSONAL TRAINING AND FITNESS PROS</div>
  <div class="abs center" style="top:58px;width:100%;font-size:2.4px;color:#f2f2f2">Your time to become a fitness pro starts now</div>
  <div class="abs center" style="left:30px;top:66px;width:46px;height:28px;background:var(--cyan);color:#fff;padding-top:4px">
    <div style="font-size:1.9px">TRAINERS</div>
    <div style="font-size:2.3px;font-weight:700;line-height:1.4;margin-top:1px">BECOME A TRAINER AND<br>GROW YOUR CLIENTS</div>
    <div style="margin:3px auto 0;width:16px;height:3px;background:#fff"></div>
  </div>
  <div class="abs center" style="left:76px;top:66px;width:46px;height:28px;background:var(--cyan-dark);color:#fff;padding-top:4px">
    <div style="font-size:1.9px">CLIENTS</div>
    <div style="font-size:2.3px;font-weight:700;line-height:1.4;margin-top:1px">FIND A TRAINER WHO<br>COMES TO YOUR HOME</div>
    <div style="margin:3px auto 0;width:16px;height:3px;background:#fff"></div>
  </div>

  <div class="feature" style="left:6px;top:100px"><i class="dot"></i><b>Motivation</b><span>Stay on track with a coach who checks in every week.</span></div>
  <div class="feature" style="left:54px;top:100px"><i class="dot"></i><b>Save time</b><span>Train at home and skip the drive to a busy gym.</span></div>
  <div class="feature" style="left:102px;top:100px"><i class="dot"></i><b>Custom plan</b><span>A program built around your goals and level.</span></div>
  <div class="feature" style="left:6px;top:132px"><i class="dot"></i><b>Expert coaches</b><span>Every trainer is certified and fully insured.</span></div>
  <div class="feature" style="left:54px;top:132px"><i class="dot"></i><b>Get results</b><span>Track progress and see real change each month.</span></div>
  <div class="feature" style="left:102px;top:132px"><i class="dot"></i><b>Good rates</b><span>Plans that fit any budget, no contracts.</span></div>

  <div class="photo" style="top:164px;height:53px;background:linear-gradient(100deg,#25292e,#4a5058 45%,#6b7077 70%,#2f3338)" role="img" aria-label="Dark gym room with equipment and a trainer"></div>
  <div class="abs caps" style="left:14px;top:171px;font-size:2.6px;color:#fff;width:56px;line-height:1.35">Search our network of trainers and book online</div>
  <div class="bullets" style="left:16px;top:181px">• Browse local profiles<br>• Read client reviews<br>• Compare session rates<br>• Book in two minutes</div>
  <div class="btn" style="left:16px;top:206px;width:16px;background:var(--cyan)">Search</div>
  <div class="abs caps" style="left:84px;top:171px;font-size:2.6px;color:#fff;width:58px;line-height:1.35">Don't have time for the gym? Let us match you with a trainer</div>
  <div class="bullets" style="left:86px;top:181px">• Tell us your goals<br>• Pick a time that works<br>• Meet your coach at home<br>• Start feeling stronger</div>
  <div class="btn" style="left:86px;top:206px;width:16px;background:var(--cyan)">Get started</div>

  <div class="abs" style="left:33px;top:225px;width:86px;height:50px;border:1.2px solid var(--cyan);border-top-color:transparent;border-bottom-color:transparent"></div>
  <div class="abs" style="left:33px;top:225px;width:5px;height:1.2px;background:var(--cyan)"></div>
  <div class="abs" style="left:114px;top:225px;width:5px;height:1.2px;background:var(--cyan)"></div>
  <div class="abs" style="left:33px;top:274px;width:5px;height:1.2px;background:var(--cyan)"></div>
  <div class="abs" style="left:114px;top:274px;width:5px;height:1.2px;background:var(--cyan)"></div>
  <div class="abs center caps" style="left:40px;top:228px;width:72px;font-size:2.4px;color:var(--cyan)">Testimonials</div>
  <div class="abs center" style="left:40px;top:231px;width:72px;font-size:4px;color:var(--cyan);font-weight:700">“</div>
  <div class="abs tiny center" style="left:42px;top:238px;width:68px;font-size:2.2px">Training at home changed my routine. My coach keeps me honest, the sessions fly by and I have more energy every single week.</div>
  <div class="abs" style="left:74px;top:254px;width:4px;height:4px;border-radius:50%;background:#b9bcc0"></div>
  <div class="abs tiny center" style="left:40px;top:259px;width:72px;font-size:2px">Jamie R.<br>Client since 2015</div>
  <div class="abs" style="left:70px;top:269px;width:12px;height:1px;background:repeating-linear-gradient(90deg,var(--cyan) 0 1.5px,transparent 1.5px 3px)"></div>

  <div class="photo" style="top:284px;height:75px;background:linear-gradient(120deg,#1d1f23,#4c5157 40%,#7a7f86 55%,#2a2d31)" role="img" aria-label="Trainer spotting a man lifting dumbbells on a bench"></div>
  <svg class="abs" style="left:69px;top:314px" width="14" height="14"><circle cx="7" cy="7" r="6" fill="none" stroke="#fff"/><path d="M5.5 4.5 L10 7 L5.5 9.5Z" fill="#fff"/></svg>

  <div class="abs center caps" style="top:366px;width:100%;font-size:2.6px;color:var(--cyan)">Most popular activities</div>
  <div class="abs" style="left:70px;top:370px;width:12px;height:.6px;background:var(--cyan)"></div>
  <div class="activity" style="left:10px;top:376px"><i class="dot"></i><b>Personal training</b></div>
  <div class="activity" style="left:43px;top:376px"><i class="dot"></i><b>Yoga</b></div>
  <div class="activity" style="left:76px;top:376px"><i class="dot"></i><b>Cardio</b></div>
  <div class="activity" style="left:109px;top:376px"><i class="dot"></i><b>Pilates</b></div>
  <div class="activity" style="left:10px;top:400px"><i class="dot"></i><b>Cycling</b></div>
  <div class="activity" style="left:43px;top:400px"><i class="dot"></i><b>Kickboxing</b></div>
  <div class="activity" style="left:76px;top:400px"><i class="dot"></i><b>Stretching</b></div>
  <div class="activity" style="left:109px;top:400px"><i class="dot"></i><b>Other sports</b></div>
  <div class="abs" style="left:128px;top:410px;width:16px;height:22px;background:var(--cyan);font-size:1.8px;color:#fff;line-height:1.7;padding:1px 2px">Boxing<br>Running<br>Dance<br>Swim</div>

  <div class="abs" style="left:0;top:429px;width:152px;height:25px;background:var(--cyan)"></div>
  <div class="abs center caps" style="top:436px;width:100%;font-size:3px;color:#fff">Join our community and become a fitness pro</div>
  <div class="btn" style="left:66px;top:443px;width:20px;background:var(--cyan-dark)">Sign up</div>
  <div class="abs" style="left:0;top:454px;width:152px;height:31px;background:var(--dark)"></div>
  <div class="abs center" style="top:459px;width:100%;font-size:3.2px;color:#fff;font-weight:700">PEAK FORM</div>
  <div class="abs tiny center" style="top:465px;width:100%;color:#9a9da2;font-size:2px">Home training across the whole region, seven days a week.<br>Home · Trainers · Activities · Contact</div>
  <div class="abs tiny center" style="top:476px;width:100%;color:#77797d;font-size:1.9px">© 2016 Peak Form. All rights reserved.</div>
</section>

<!-- Runner website -->
<section class="site runner" style="left:145px;top:590px;width:147px;height:486px">
  <div class="abs" style="left:0;top:0;width:147px;height:12px;background:#fff"></div>
  <div class="abs" style="left:32px;top:4px;font-size:2.1px;color:#9a9da2;word-spacing:11px">Home About Classes Coaches Contact</div>
  <div class="abs" style="left:118px;top:4.5px;width:3px;height:3px;border-radius:50%;background:#bbb"></div>
  <div class="abs" style="left:123px;top:4.5px;width:3px;height:3px;border-radius:50%;background:#bbb"></div>
  <div class="photo" style="top:12px;height:95px;background:linear-gradient(110deg,#2f2b24,#6b5630 40%,#b88d32 60%,#dcae45)" role="img" aria-label="Woman in a yellow jacket running past a wall"></div>
  <div class="abs" style="left:30px;top:46px;font-size:4.2px;color:#fff;letter-spacing:.4px;line-height:1.35;width:52px">LOREM IPSUM DOLOR SIT AMET CONSECTETUR ADIPISCING ELIT</div>
  <div class="abs" style="left:30px;top:78px;width:20px;height:4px;border:0.6px solid #fff;font-size:1.8px;color:#fff;text-align:center;line-height:3px">READ MORE</div>

  <div class="abs" style="left:0;top:107px;width:147px;height:33px;background:var(--lime)"></div>
  <div class="abs center caps" style="top:112px;width:100%;font-size:2.2px;color:#555">About</div>
  <div class="abs tiny center" style="left:22px;top:117px;width:103px;font-size:2.1px;color:#555">Strength, speed and focus for every runner in town. We plan each session around you so every week brings a clear step forward.</div>

  <div class="photo" style="top:140px;height:82px;background:linear-gradient(100deg,#19191b,#3f3f42 40%,#5c5c60 55%,#232325)" role="img" aria-label="Woman training with dumbbells in a dark studio"></div>
  <div class="abs" style="left:45px;top:156px;width:37px;height:41px;background:#fff;padding:5px 3px 0;text-align:center">
    <div class="caps" style="font-size:2.3px">Personal trainer</div>
    <div class="tiny" style="font-size:1.9px;margin-top:2px">One to one sessions built around your own goals and pace.</div>
  </div>
  <div class="abs" style="left:82px;top:156px;width:37px;height:41px;background:var(--lime);padding:5px 3px 0;text-align:center">
    <div class="caps" style="font-size:2.3px">Group training</div>
    <div class="tiny" style="font-size:1.9px;margin-top:2px;color:#555">Small classes with big energy for runners of all levels.</div>
  </div>

  <div class="abs" style="left:0;top:222px;width:147px;height:33px;background:var(--peach)"></div>
  <div class="abs center caps" style="top:227px;width:100%;font-size:2.2px;color:#6a5048">Classes</div>
  <div class="abs tiny center" style="left:22px;top:232px;width:103px;font-size:2.1px;color:#6a5048">Classes run every week for beginners and pros alike. Join a morning run, a strength hour or a weekend long run.</div>

  <div class="abs" style="left:0;top:255px;width:147px;height:79px;background:var(--teal)"></div>
  <div class="abs caps center" style="left:51px;top:267px;width:15px;height:15px;background:#fff;font-size:2px;padding-top:5px">Lorem<br>ipsum</div>
  <div class="abs caps center" style="left:66px;top:267px;width:15px;height:15px;background:#fff;font-size:2px;padding-top:5px;color:var(--orange)">Lorem<br>ipsum</div>
  <div class="abs caps center" style="left:81px;top:267px;width:15px;height:15px;background:#fff;font-size:2px;padding-top:5px">Lorem<br>ipsum</div>
  <div class="abs caps center" style="left:66px;top:282px;width:15px;height:15px;background:#fff;font-size:2px;padding-top:5px">Lorem<br>ipsum</div>
  <div class="abs caps center" style="left:81px;top:282px;width:15px;height:15px;background:var(--lime);font-size:2px;padding-top:5px">Lorem<br>ipsum</div>
  <div class="abs caps center" style="left:81px;top:297px;width:15px;height:15px;background:#fff;font-size:2px;padding-top:5px">Lorem<br>ipsum</div>

  <div class="photo" style="top:334px;height:68px;background:linear-gradient(90deg,#171718,#3b3b3e 55%,#59595d 70%,#1e1e20)" role="img" aria-label="Athlete resting in a dark gym"></div>
  <div class="abs center" style="left:20px;top:361px;width:107px;font-size:2.6px;color:#fff;font-weight:700;line-height:1.5">LOREM IPSUM DOLOR SIT AMET, CONSECTETUR ADIPISCING ELIT. VESTIBULUM PORTTITOR VITAE ILLAMO, SEMPER RISUS CONSECTETUR.</div>

  <div class="abs" style="left:0;top:402px;width:147px;height:84px;background:var(--mint)"></div>
  <div class="abs center caps" style="top:407px;width:100%;font-size:2.2px;color:#2c6a5e">Contact</div>
  <div class="abs" style="left:49px;top:414px;width:49px;height:3.4px;background:#fff;font-size:1.8px;color:#999;padding-left:1.5px;line-height:3.4px">Name</div>
  <div class="abs" style="left:49px;top:419px;width:49px;height:3.4px;background:#fff;font-size:1.8px;color:#999;padding-left:1.5px;line-height:3.4px">Email</div>
  <div class="abs" style="left:49px;top:424px;width:49px;height:11px;background:#fff;font-size:1.8px;color:#999;padding:1px 1.5px">Message</div>
  <div class="btn" style="left:88px;top:437px;width:10px;background:#fff;color:#2c6a5e">Send</div>
  <div class="abs tiny center" style="left:35px;top:445px;width:77px;font-size:2px;color:#2c6a5e">Call or write any day, we reply within a few hours.<br>(555) 014-7781<br>run@peakstride.test</div>
  <div class="abs" style="left:64px;top:466px;width:4px;height:4px;border-radius:50%;background:#fff"></div>
  <div class="abs" style="left:70px;top:466px;width:4px;height:4px;border-radius:50%;background:#fff"></div>
  <div class="abs" style="left:76px;top:466px;width:4px;height:4px;border-radius:50%;background:#fff"></div>
</section>

<!-- Tire website -->
<section class="site tires" style="left:452px;top:62px;width:264px;height:1014px">
  <div class="abs" style="left:0;top:0;width:264px;height:27px;background:var(--orange)"></div>
  <div class="abs" style="left:38px;top:3px;width:26px;height:26px;border-radius:50%;background:var(--yellow);font-family:Oswald,sans-serif;font-size:4.6px;color:#fff;text-align:center;line-height:26px">ROADLY</div>
  <div class="nav" style="left:86px;top:7px;text-transform:none">Open daily 7am – 9pm</div>
  <div class="nav" style="left:130px;top:7px;text-transform:none">hello@roadlytires.test</div>
  <div class="nav" style="left:180px;top:7px">(555) 014-2290</div>
  <div class="nav" style="left:220px;top:7px;text-transform:none">Follow us</div>
  <div class="nav" style="left:82px;top:18px;font-weight:500">Home</div>
  <div class="nav" style="left:108px;top:18px">Who we are</div>
  <div class="nav" style="left:146px;top:18px">Services</div>
  <div class="nav" style="left:178px;top:18px">Contact</div>
  <div class="nav" style="left:206px;top:18px">Tire size calculator</div>
  <div class="photo" style="top:27px;height:137px;background:linear-gradient(165deg,#e3a42c,#b4882f 35%,#7a6a45 60%,#5b6a52 85%,#6e7d55)" role="img" aria-label="Mobile tire service van and car parked on a road"></div>
  <div class="abs" style="left:140px;top:58px;width:112px;height:70px;background:rgba(196,150,54,.88)"></div>
  <div class="abs t-head" style="left:146px;top:65px;font-size:9px;color:#fff;background:var(--yellow);padding:0 2px">24 HOURS</div>
  <div class="abs t-head" style="left:146px;top:82px;font-size:5px;color:#fff;line-height:1.2">MOBILE TIRE REPAIR SERVICE<br>THAT COMES TO YOU</div>
  <div class="abs" style="left:146px;top:96px;font-size:2.6px;color:#fff;width:98px;line-height:1.45">Serving all of Harbor County. We come to you fast, on the road, at home or at work, so you can get moving again today.</div>
  <div class="btn" style="left:146px;top:115px;width:34px;background:var(--orange);height:5px;line-height:5px">Call and book now</div>
  <div class="abs" style="left:0;top:164px;width:264px;height:32px;background:var(--gold)"></div>
  <div class="abs t-head" style="left:28px;top:173px;font-size:7px;color:#fff">GET A QUOTE</div>
  <div class="abs" style="left:77px;top:175px;width:40px;height:8px;background:#fff;font-size:2.2px;color:#999;padding:2.6px 2px">Email</div>
  <div class="abs" style="left:120px;top:175px;width:40px;height:8px;background:#fff;font-size:2.2px;color:#999;padding:2.6px 2px">Select service ▾</div>
  <div class="abs" style="left:163px;top:175px;width:40px;height:8px;background:#fff;font-size:2.2px;color:#999;padding:2.6px 2px">Select time ▾</div>
  <div class="btn" style="left:206px;top:175px;width:30px;height:8px;line-height:8px;background:var(--orange)">Submit now</div>

  <div class="abs" style="left:28px;top:217px;width:206px;height:99px;background:linear-gradient(100deg,#9fb6c8,#d4e0e8 50%,#b2c4a3)" role="img" aria-label="Mobile tire shop box truck parked by trees"></div>
  <svg class="abs" style="left:28px;top:217px" width="206" height="99"><polygon points="0,0 120,0 90,99 0,99" fill="#f2a92c"/></svg>
  <div class="abs t-head" style="left:38px;top:232px;font-size:5px;color:#fff;line-height:1.05;width:90px">GETTING NEW TIRES COULDN'T BE EASIER WITH OUR MOBILE TIRE SHOP</div>
  <div class="abs" style="left:38px;top:252px;font-size:2.5px;color:#fff;width:80px;line-height:1.55">Got a flat on the road? Give us a call and our tire truck will be with you in no time. Need new tires? We bring them to your door, fitted and balanced on the spot. Ask for a quote or book a time slot online.</div>
  <div class="btn" style="left:38px;top:284px;width:34px;height:7px;line-height:7px;background:var(--orange)">Learn more</div>

  <div class="abs" style="left:0;top:338px;width:264px;height:105px;background:var(--gold)"></div>
  <div class="abs" style="left:105px;top:338px;width:54px;height:52px;background:linear-gradient(120deg,#333335,#6a6a6c 60%,#4a4a4c)" role="img" aria-label="Mechanic working on a wheel"></div>
  <div class="abs t-head" style="left:105px;top:360px;width:54px;text-align:center;font-size:7px;color:#fff">SERVICES</div>
  <div class="t-cell" style="left:4px;top:338px"><i></i>Car, truck &amp; bus tire road service</div>
  <div class="t-cell" style="left:54px;top:338px"><i></i>Install tires</div>
  <div class="t-cell" style="left:161px;top:338px"><i></i>New &amp; used tires, all season, all terrain</div>
  <div class="t-cell" style="left:212px;top:338px"><i></i>Tire rotation &amp; balanced tires on site</div>
  <div class="abs" style="left:53px;top:390px;width:53px;height:53px;background:var(--yellow)"></div>
  <div class="t-cell" style="left:3px;top:390px"><i></i>Tire replacement on the spot</div>
  <div class="t-cell" style="left:55px;top:390px"><i></i>Fleet, retail &amp; commercial tires</div>
  <div class="t-cell" style="left:107px;top:390px"><i></i>Rim lock removal &amp; stripped wheel lug nut</div>
  <div class="t-cell" style="left:161px;top:390px"><i></i>Valve stem replacement</div>
  <div class="t-cell" style="left:212px;top:390px"><i></i>Flat tires fix on site</div>

  <div class="abs t-head" style="top:456px;width:100%;text-align:center;font-size:7.5px;color:var(--orange)">FREQUENTLY ASKED QUESTIONS</div>
  <div class="abs" style="left:128px;top:468px;width:7px;height:7px;border-radius:50%;background:var(--grey)"></div>
  <div class="faq" style="top:480px">Q. How fast can your tire truck reach me on the road?</div>
  <div class="abs" style="left:76px;top:490px;width:176px;font-size:2.2px;color:#888;line-height:1.55;padding:1px 4px">Most calls in the county are served within the hour. Our trucks carry new and used tires, tools and balancing gear on board, so the whole job is done where you are parked.</div>
  <div class="faq" style="top:512px">Q. Do you repair fleet, bus and commercial tires?</div>
  <div class="faq" style="top:525px">Q. Can I book a time slot for tire fitting online?</div>
  <div class="faq" style="top:538px">Q. Which payment methods do you accept on site?</div>

  <div class="abs" style="left:0;top:556px;width:264px;height:119px;background:linear-gradient(110deg,#dcdcdc,#9a9a9a 35%,#555 60%,#1e1e1e)" role="img" aria-label="Black and white photo of a worker changing a truck tire"></div>
  <div class="abs" style="left:46px;top:595px;width:172px;height:46px;background:rgba(255,255,255,.6)"></div>
  <div class="abs" style="left:49px;top:598px;width:40px;height:40px;background:linear-gradient(160deg,#c99b7c,#8a6650)" role="img" aria-label="Customer portrait"></div>
  <div class="abs t-head" style="left:96px;top:600px;font-size:3.4px;color:#333">LOREM M DOE</div>
  <div class="abs" style="left:96px;top:605px;font-size:2.2px;color:#555">Customer</div>
  <div class="abs" style="left:96px;top:609px;font-size:3px;color:var(--yellow);letter-spacing:.4px">★★★★</div>
  <div class="abs" style="left:96px;top:615px;font-size:2.3px;color:#333;width:116px;line-height:1.55">Fast, friendly and fair. They fixed my flat in the driveway before work, showed me the damage and had me back on the road in twenty minutes. I will call them again.</div>
  <div class="abs" style="left:30px;top:614px;width:7px;height:7px;border-radius:50%;background:var(--yellow)"></div>
  <div class="abs" style="left:226px;top:614px;width:7px;height:7px;border-radius:50%;background:var(--yellow)"></div>

  <div class="abs" style="left:0;top:675px;width:264px;height:51px;background:var(--yellow)"></div>
  <div class="abs t-head" style="top:688px;width:100%;text-align:center;font-size:7.5px;color:#fff">TIRE SIZE CALCULATOR</div>
  <div class="btn" style="left:118px;top:702px;width:28px;height:7px;line-height:7px;background:var(--orange)">Calculate now</div>

  <div class="abs" style="left:0;top:726px;width:264px;height:113px;background:linear-gradient(180deg,#e2e8ef,#c6d0db)" role="img" aria-label="Faded city skyline"></div>
  <div class="abs t-head" style="top:740px;width:100%;text-align:center;font-size:7.5px;color:var(--orange);line-height:1.55">RUN BY HARBOR COUNTY LOCALS FOR<br>HARBOR COUNTY LOCALS</div>
  <div class="abs" style="left:56px;top:768px;width:152px;font-size:2.5px;color:#555;text-align:center;line-height:1.6">Roadly Tires isn't just the best mobile tire service in Harbor County. We help you get back to work in Bay Town and the towns around it, because we live here too and care about our neighbours.<br><br>By focusing on our own area, you can be sure help is always close by, and that the people who come to you know these roads and want you safe on them.</div>

  <div class="abs" style="left:0;top:839px;width:264px;height:63px;background:#3a3a3c"></div>
  <div class="abs" style="left:30px;top:850px;width:26px;height:26px;border-radius:50%;background:var(--orange);font-family:Oswald,sans-serif;font-size:4.6px;color:#fff;text-align:center;line-height:26px">ROADLY</div>
  <div class="abs" style="left:28px;top:883px;width:40px;height:7px;border:0.7px solid #fff;font-size:2.1px;color:#fff;text-align:center;line-height:5.6px">CONNECT WITH US</div>
  <div class="abs t-head" style="left:114px;top:851px;font-size:3px;color:#fff">SITE LINKS</div>
  <div class="abs" style="left:116px;top:858px;font-size:2.3px;color:#bbb;line-height:1.9">› Home<br>› Who we are<br>› Services<br>› Contact<br>› Tire size calculator</div>
  <div class="abs t-head" style="left:180px;top:851px;font-size:3px;color:#fff">CONTACT US</div>
  <svg class="abs" style="left:180px;top:858px" width="5" height="6"><path d="M2.5 6 C0 3,0 2.5,0 2.5 A2.5 2.5 0 0 1 5 2.5 C5 2.5,5 3,2.5 6Z" fill="#f2b232"/></svg>
  <div class="abs" style="left:188px;top:858px;font-size:2.3px;color:#bbb;line-height:1.5">12 Harbor Way, Bay Town<br>United States</div>
  <svg class="abs" style="left:180px;top:869px" width="5" height="5"><path d="M1 0.5 L2 0.5 L2.6 1.8 L1.9 2.4 Q2.5 3.4 3.3 3.1 L3.9 2.5 L4.6 3.2 L4.3 4.4 Q1.5 4.6 0.5 1.5Z" fill="#f2b232"/></svg>
  <div class="abs" style="left:188px;top:869px;font-size:2.3px;color:#bbb">(555) 014-2290</div>
  <svg class="abs" style="left:180px;top:878px" width="5" height="4"><rect x=".3" y=".3" width="4.4" height="3.4" fill="none" stroke="#f2b232" stroke-width=".6"/><path d="M.3 .3 L2.5 2.2 L4.7 .3" fill="none" stroke="#f2b232" stroke-width=".6"/></svg>
  <div class="abs" style="left:188px;top:878px;font-size:2.3px;color:#bbb">hello@roadlytires.test</div>

  <div class="abs" style="left:0;top:902px;width:264px;height:98px;background:linear-gradient(135deg,#eaede5,#dde3db 60%,#e5e8e1)" role="img" aria-label="Street map of the service area"></div>
  <svg class="abs" style="left:141px;top:940px" width="6" height="8"><path d="M3 8 C0 4,0 3,0 3 A3 3 0 0 1 6 3 C6 3,6 4,3 8Z" fill="#d9342b"/></svg>
  <div class="abs" style="left:149px;top:942px;font-size:2.2px;color:#c0392b;font-weight:700">12 Harbor Way</div>

  <div class="abs" style="left:0;top:1000px;width:264px;height:14px;background:var(--orange)"></div>
  <div class="abs" style="left:28px;top:1005px;font-size:2.3px;color:#fff">© 2016 Roadly Tires. All rights reserved</div>
  <div class="abs" style="left:112px;top:1005px;font-size:2.3px;color:#fff">Designed by Harbor Studio</div>
  <div class="abs" style="left:172px;top:1005px;font-size:2.3px;color:#fff">We accept</div>
  <div class="abs" style="left:198px;top:1004px;width:8px;height:5px;background:#fff"></div>
  <div class="abs" style="left:208px;top:1004px;width:8px;height:5px;background:#fff"></div>
  <div class="abs" style="left:218px;top:1004px;width:8px;height:5px;background:#fff"></div>
  <div class="abs" style="left:228px;top:1004px;width:8px;height:5px;background:#fff"></div>
</section>

</body>
</html>
```